Retail Product Label mushrooms

We wish to make a 2x3 inch rectangle product label as shown in the PDF. We wish to use the entire space available to make the words and logo as large as possible. We wish the top 1/3rd to be red with the logo inside it. We wish the bottom 2/3rds to be white with the product name inserted. We still need allocations for the barcode weight etc. as shown in the image uploaded.

Target Market(s)

Retail Label

Industry/Entity Type

Fresh Produce mushrooms

Colors
EB3D1F
EC4F4E
F09395
F8D3D4
FCEDEE

Requirements
Must have
• All included
Nice to have
• Shiitake label is best example of what we seek in a rectangle design
Should not have
• You must include all information in the example (weight barcode area, etc.)

```html
<!DOCTYPE html>
<html lang="en">
<head>
<meta charset="utf-8">
<title>Bracken Sliced Mushrooms – Retail Label</title>
<link href="https://fonts.googleapis.com/css2?family=Staatliches&family=Roboto+Slab:wght@500;700&display=swap" rel="stylesheet">
<style>
  :root {
    --stage: #5f6062;
    --label-paper: #f6f6f5;
    --brand-red: #eb3d1f;
    --ink: #141414;
    --white: #ffffff;
  }
  html, body {
    margin: 0;
    padding: 0;
    width: 1200px;
    height: 997px;
    overflow: hidden;
    background: var(--stage);
  }
  .label {
    position: absolute;
    left: 300px;
    top: 48px;
    width: 798px;
    height: 1196px;
    background: var(--label-paper);
    transform: scale(0.7525);
    transform-origin: 0 0;
  }
  .label__frame {
    position: absolute;
    left: 30px;
    top: 35px;
    width: 737px;
    height: 1126px;
    border: 3px solid var(--brand-red);
    border-radius: 10px;
    box-sizing: border-box;
  }
  .brand-band {
    position: absolute;
    left: 50px;
    top: 56px;
    width: 698px;
    height: 312px;
    background: var(--brand-red);
    border-radius: 8px 8px 0 0;
    display: flex;
    align-items: center;
    justify-content: center;
  }
  .brand-band__name {
    font-family: "Staatliches", sans-serif;
    font-size: 190px;
    line-height: 1;
    color: var(--white);
    letter-spacing: 4px;
    margin-top: 12px;
  }
  .brush-stripe {
    position: absolute;
    left: 50px;
    top: 382px;
    width: 698px;
    height: 24px;
  }
  .product-name {
    position: absolute;
    left: 50px;
    top: 440px;
    width: 698px;
    margin: 0;
    text-align: center;
    font-family: "Staatliches", sans-serif;
    font-weight: 400;
    font-size: 178px;
    line-height: 148px;
    color: var(--ink);
  }
  .variety {
    position: absolute;
    left: 94px;
    top: 781px;
    width: 610px;
    height: 49px;
    border-top: 2px solid var(--brand-red);
    border-bottom: 2px solid var(--brand-red);
    box-sizing: border-box;
    display: flex;
    align-items: center;
    justify-content: center;
    font-family: "Roboto Slab", serif;
    font-weight: 700;
    font-size: 22px;
    letter-spacing: 11px;
    color: var(--ink);
  }
  .info-table {
    position: absolute;
    left: 64px;
    top: 901px;
    width: 667px;
    height: 226px;
    border: 3px solid var(--ink);
    border-radius: 8px;
    box-sizing: border-box;
    display: grid;
    grid-template-columns: 376px 1fr;
    grid-template-rows: 62px 57px 56px 1fr;
    font-family: "Roboto Slab", serif;
    font-weight: 500;
    color: var(--ink);
  }
  .info-table__cell {
    display: flex;
    align-items: center;
    padding-left: 14px;
    font-size: 24px;
    border-right: 3px solid var(--ink);
    border-bottom: 3px solid var(--ink);
  }
  .info-table__cell:nth-child(3) { border-bottom: 3px solid var(--ink); }
  .info-table__barcode-area {
    grid-column: 2;
    grid-row: 1 / 4;
    border-bottom: 3px solid var(--ink);
  }
  .info-table__website {
    grid-column: 1 / 3;
    display: flex;
    align-items: center;
    justify-content: center;
    font-size: 24px;
    letter-spacing: 9px;
  }
</style>
</head>
<body>
  <div class="label">
    <div class="label__frame"></div>

    <div class="brand-band">
      <span class="brand-band__name">BRACKEN</span>
    </div>

    <svg class="brush-stripe" viewBox="0 0 698 24" preserveAspectRatio="none" aria-hidden="true">
      <polygon fill="#eb3d1f" points="0,3 60,1 140,4 230,2 320,5 410,1 500,4 590,2 698,3 698,14 660,17 610,15 560,20 500,16 440,21 380,17 320,22 260,18 200,21 140,17 80,20 30,16 0,19"/>
    </svg>

    <h1 class="product-name">Product<br>Name</h1>

    <div class="variety">SLICED MUSHROOMS</div>

    <div class="info-table">
      <div class="info-table__cell">PRODUCT OF USA</div>
      <div class="info-table__barcode-area"></div>
      <div class="info-table__cell">KEEP REFRIDGERATED</div>
      <div class="info-table__cell">NET WT:</div>
      <div class="info-table__website">WWW.WEBSITE.COM</div>
    </div>
  </div>
</body>
</html>
```